Package design for small honey and vegetable farm

I would like to have a unique design for the packaging of our honey and vegetables. I have attached the logo from our farm "Willowbrook Acres" that should be on the packaging for both the honey and the vegetables

For the honey the writing, "100% pure organic honey" must be on the packaging in some place. As well as "from the busy bees at Willowbrook Acres". I have attached some designs that I like.

For the vegetables. The design will need to go on a box like the one in the attached image. The phrase "Organically Grown" should be on the package. I would like the background color of the package to be black. I think I would also like to see some stylized vegetables (tomatoes in particular) on the package.

I would like to be able to get all the colors (RGB) used in the designs so I can pass them on to printers.

Industry/Entity Type

Farm

Colors
fbee3e

Requirements
Must have
• For the honey, the package it must say "100% pure organic honey".
• For the vegetables I would like the background color to be black. I would also like some stylized vegetables (tomatoes in particular) added to the package.

```html
<!DOCTYPE html>
<html lang="en">
<head>
<meta charset="utf-8">
<title>Willowbrook Acres – Honey Label and Vegetable Box</title>
<link rel="stylesheet" href="https://fonts.googleapis.com/css2?family=Exo+2:wght@300;400;600&display=swap">
<style>
  :root {
    --page: #ffffff;
    --label-black: #1a1a1a;
    --label-border: #f7941d;
    --honeycomb: #2f2f2f;
    --honey-orange: #f7941d;
    --brand-yellow: #fbee3e;
    --box-grey: #474747;
    --box-edge: #3a3a3a;
    --leaf-green: #8dc63f;
    --veg-red: #d9261c;
    --veg-yellow: #f6b312;
  }
  * { margin: 0; padding: 0; box-sizing: border-box; }
  html, body { width: 1200px; height: 1062px; overflow: hidden; background: var(--page); }
  body { font-family: "Exo 2", sans-serif; position: relative; }

  .honey-label { position: absolute; left: 414px; top: 40px; width: 372px; height: 432px; }

  .box-panel {
    position: absolute;
    top: 560px;
    height: 340px;
    background: var(--box-grey);
    border-top: 6px solid var(--box-edge);
  }
  .box-end { left: 40px; width: 340px; }
  .box-front { left: 410px; width: 750px; }

  .brand-mark {
    position: absolute;
    display: flex;
    align-items: center;
    gap: 12px;
    color: var(--brand-yellow);
    font-weight: 400;
    font-size: 40px;
    line-height: 1.05;
  }
  .brand-dot { width: 18px; height: 18px; border-radius: 50%; background: var(--brand-yellow); flex: none; }
  .box-end .brand-mark { left: 40px; top: 70px; width: 270px; }
  .box-front .brand-mark { left: 50px; top: 110px; width: 280px; }

  .tagline {
    position: absolute;
    color: var(--leaf-green);
    font-weight: 300;
    font-size: 34px;
    white-space: nowrap;
  }
  .box-end .tagline { left: 46px; top: 210px; }
  .box-front .tagline { left: 60px; top: 232px; }

  .vegetable-art {
    position: absolute;
    left: 370px;
    top: 70px;
    width: 350px;
    height: 200px;
    border-radius: 90px;
    background: linear-gradient(90deg, var(--veg-red) 0%, var(--veg-yellow) 38%, var(--veg-red) 62%, #e4372a 100%);
  }
</style>
</head>
<body>

<svg class="honey-label" viewBox="0 0 372 432" role="group" aria-label="Honey jar label">
  <defs>
    <clipPath id="hex-clip">
      <polygon points="186,0 372,108 372,324 186,432 0,324 0,108"/>
    </clipPath>
    <linearGradient id="drop-fill" x1="0" y1="0" x2="0" y2="1">
      <stop offset="0" stop-color="#fbe03e"/>
      <stop offset="1" stop-color="#f59a1b"/>
    </linearGradient>
    <path id="ring" d="M119,317 A95,95 0 1 1 253,317"/>
  </defs>
  <polygon points="186,0 372,108 372,324 186,432 0,324 0,108" fill="var(--label-black)"/>
  <g clip-path="url(#hex-clip)">
    <path d="M0,232 Q186,180 372,232 L372,432 L0,432 Z" fill="var(--honeycomb)" role="img" aria-label="Honeycomb pattern"/>
  </g>
  <polygon points="186,2 370,109 370,323 186,430 2,323 2,109" fill="none" stroke="var(--label-border)" stroke-width="3"/>

  <circle cx="82" cy="126" r="7" fill="var(--brand-yellow)"/>
  <text x="196" y="135" text-anchor="middle" font-family="Exo 2, sans-serif" font-weight="400" font-size="25" fill="var(--brand-yellow)">Willowbrook Acres</text>

  <text font-family="Exo 2, sans-serif" font-weight="300" font-size="27" fill="var(--honey-orange)">
    <textPath href="#ring" startOffset="50%" text-anchor="middle">100% pure organic honey</textPath>
  </text>

  <path d="M186,205 C200,232 222,252 222,275 A36,36 0 0 1 150,275 C150,252 172,232 186,205 Z" fill="url(#drop-fill)"/>

  <text x="186" y="345" text-anchor="middle" font-family="Exo 2, sans-serif" font-weight="300" font-size="15" fill="var(--brand-yellow)">from the busy bees</text>
  <text x="186" y="365" text-anchor="middle" font-family="Exo 2, sans-serif" font-weight="300" font-size="15" fill="var(--brand-yellow)">at Willowbrook Acres</text>
</svg>

<section class="box-panel box-end" aria-label="Vegetable box end panel">
  <div class="brand-mark"><span class="brand-dot"></span><span>Willowbrook Acres</span></div>
  <p class="tagline">Organically Grown</p>
</section>

<section class="box-panel box-front" aria-label="Vegetable box front panel">
  <div class="brand-mark"><span class="brand-dot"></span><span>Willowbrook Acres</span></div>
  <p class="tagline">Organically Grown</p>
  <div class="vegetable-art" role="img" aria-label="Illustration of a red pepper, a yellow pepper and two tomatoes"></div>
</section>

</body>
</html>
```